Acupuncture Medspa needs a business card design

I need a business card design that looks professional, has a spa-like quality and can offer a promo on the back. Initial promo is "First session free". The tagline of NeedleNook is: Refresh, Restore, Rejuvenate.

NeedleNook is a membership-based acupuncture medspa that offers acupuncture, cupping, and herbal therapies. Members choose between the "Refresh" membership which is for stress relief, or "Restore" which is for treating health conditions, and lastly "Rejuvenate" which is for natural facial enhancement.

Industry/Entity Type

Health And Wellness

Contact Information for Business Card

Coral Haskins, MAC, L.Ac.
612-555-0193
www.needlenook-example.com

Font styles to use
Serif
Sans Serif

Colors

Designer to choose colors to be used in the design.

Requirements
Must have
• The project must have NeedleNook logo, promo on the back, and contact information
Nice to have
• I would like to see the colors of the logo used.

```html
<!DOCTYPE html>
<html lang="en">
<head>
<meta charset="utf-8">
<title>NeedleNook Business Card</title>
<link href="https://fonts.googleapis.com/css2?family=Lato:wght@400;700&display=swap" rel="stylesheet">
<style>
  :root {
    --stage: #1b1b1c;
    --card: #0f0f10;
    --teal: #2b8e8c;
    --silver: #d9d9d9;
    --text: #f2f2f2;
    --rule: #8a8a8a;
  }
  * { box-sizing: border-box; margin: 0; padding: 0; }
  html, body { width: 1200px; height: 900px; overflow: hidden; }
  body {
    background: var(--stage);
    font-family: "Lato", sans-serif;
    position: relative;
  }
  .card {
    position: absolute;
    left: 337px;
    width: 525px;
    height: 300px;
    background: var(--card);
    border-radius: 18px;
    box-shadow: 0 10px 30px rgba(0,0,0,.55);
  }
  .card--back { top: 120px; }
  .card--front { top: 470px; }

  /* back */
  .back-mark {
    position: absolute;
    left: 0; right: 0; top: 78px;
    display: flex; align-items: center; justify-content: center; gap: 14px;
  }
  .back-mark__dot {
    width: 22px; height: 22px; border-radius: 50%;
    border: 2px solid var(--silver);
  }
  .back-mark__name {
    font-weight: 700; font-size: 34px; letter-spacing: 1px; color: var(--silver);
  }
  .promo {
    position: absolute;
    top: 200px; left: 0; right: 0;
    text-align: center;
    color: var(--text);
    font-size: 14px;
    letter-spacing: 1px;
  }

  /* front */
  .brand {
    position: absolute;
    top: 52px; right: 42px;
    display: flex; align-items: center; gap: 12px;
  }
  .brand__dot {
    width: 20px; height: 20px; border-radius: 50%; background: var(--teal);
  }
  .brand__name {
    font-weight: 700; font-size: 42px; letter-spacing: 1px; color: var(--teal);
  }
  .brand-rule {
    position: absolute; top: 118px; left: 220px; right: 42px;
    height: 1px; background: var(--rule);
  }
  .holder {
    position: absolute; top: 160px; left: 30px; right: 42px;
    display: flex; align-items: center; gap: 10px;
  }
  .holder__name {
    color: var(--teal); font-weight: 700; font-size: 17px; letter-spacing: .5px;
    white-space: nowrap;
  }
  .holder__rule { flex: 1; height: 1px; background: var(--rule); }
  .contacts {
    position: absolute; top: 200px; left: 36px;
    list-style: none;
  }
  .contacts li {
    display: flex; align-items: center; gap: 10px;
    color: var(--text); font-size: 15px; line-height: 24px;
  }
  .contacts svg { width: 13px; height: 13px; fill: var(--teal); flex: none; }
  .tagline {
    position: absolute; top: 202px; right: 42px;
    color: var(--text); font-size: 13px; letter-spacing: .6px;
  }
</style>
</head>
<body>
  <section class="card card--back" aria-label="Card back">
    <div class="back-mark">
      <span class="back-mark__dot"></span>
      <span class="back-mark__name">NeedleNook</span>
    </div>
    <p class="promo">FIRST SESSION FREE</p>
  </section>

  <section class="card card--front" aria-label="Card front">
    <div class="brand">
      <span class="brand__dot"></span>
      <span class="brand__name">NeedleNook</span>
    </div>
    <div class="brand-rule"></div>

    <div class="holder">
      <span class="holder__name">CORAL HASKINS, MAC, L.AC.</span>
      <span class="holder__rule"></span>
    </div>

    <ul class="contacts">
      <li>
        <svg viewBox="0 0 16 16" aria-hidden="true"><path d="M3 1l3 3-1.5 2a9 9 0 0 0 5.5 5.5L12 10l3 3-2 2C7 15 1 9 1 3z"/></svg>
        612-555-0193
      </li>
      <li>
        <svg viewBox="0 0 16 16" aria-hidden="true"><path d="M1 3h14v10H1zM2 4l6 5 6-5v1L8 10 2 5z" fill-rule="evenodd"/></svg>
        coral@needlenook-example.com
      </li>
      <li>
        <svg viewBox="0 0 16 16" aria-hidden="true"><circle cx="8" cy="8" r="7"/></svg>
        www.needlenook-example.com
      </li>
    </ul>

    <p class="tagline">REFRESH | RESTORE | REJUVENATE</p>
  </section>
</body>
</html>
```